Business Intelligence Application - Reporting Menu and Report Criteria Design

Looking for a fresh, effective and user friendly view for the menu structure and reporting criteria screen format for a business reporting application. Initial format completed, content structure is in place, but we need the 'wow' design.. as its a serious professional report/BI tool it has to fall within certain guidelines for clarity and graphics..but we want it to be slick, friendly, great user experience. There is a large amount of complex content to fit into a small space and we need it to be very inviting, modern and intuitive.. If interested, please review the attachment. We have live screens in operation, but feel these could be improved and looking forward to seeing what great creative suggestions could be made. Please review work done to date in the attached.. We are not looking for a total re-design of everything, all the basic business content/structure is there.. but tell us what we could do to improve this in terms of graphic design... particularly the criteria screens.. thanks!
Updates

Reason: Need a few more days to review designs - thanks for all submissions so far, we will make a selection shortly.

Target Market(s)

Business analysts, hotel operations teams, finance analysts hospitality industry

Industry/Entity Type

Hospitality

Coding

Coded - Design and coding required

Number of Pages Required

4 page

Font styles to use
Sans Serif
Other font styles liked:
• Candara, please see example in deck

Colors
3276b5
3176b5
0255a3
85acd3
33a6d7
cee9f5
85cae6

Requirements
Must have
• sharp clear, logical menu structure, (currently it has 'clicks to sub-menus, we need hover over, slide to sub-menus..) colour, styling.. and most focus on revision of criteria.. right now is somewhat heavy, cumbersome.. keep colour and friendly intuitive process steps.. its heavy analytical stuff.. best of luck!
Should not have
• No grey fonts on white or grey screens! many business apps are not readable or sharp.. or fonts are too small.. colourless, so please avoid that.. see our deck - sharp dark (navy) or black fonts on white, or light shading..

```html
<!DOCTYPE html>
<html lang="en">
<head>
<meta charset="utf-8">
<title>Silver Harbor Hotels &amp; Suites – Report Criteria</title>
<link href="https://fonts.googleapis.com/css2?family=Cabin:wght@400;500;600&display=swap" rel="stylesheet">
<style>
  :root{
    --navy:#0255a3;
    --brand:#3276b5;
    --sky:#33a6d7;
    --sky-light:#cee9f5;
    --ink:#111a26;
    --white:#ffffff;
    --line:#8a8f96;
  }
  *{box-sizing:border-box;margin:0;padding:0}
  html,body{width:1200px;height:938px;overflow:hidden;background:var(--white)}
  body{position:relative;font-family:"Cabin",sans-serif;color:var(--ink)}

  .topbar{position:absolute;left:0;top:0;width:1200px;height:60px;background:var(--navy);color:var(--white)}
  .brand{position:absolute;left:48px;top:15px;display:flex;align-items:center;gap:9px;font-size:20px;font-weight:500;letter-spacing:-.2px}
  .brand-dot{width:28px;height:28px;border-radius:50%;background:var(--white)}
  .welcome{position:absolute;left:557px;top:22px;font-size:13px}
  .date{position:absolute;left:669px;top:22px;font-size:13px}
  .top-btn{position:absolute;top:11px;width:107px;height:37px;background:var(--sky);color:var(--white);font-size:12.5px;font-weight:600;display:flex;align-items:center;justify-content:center;letter-spacing:.3px}
  .top-btn.intel{left:834px}
  .top-btn.planning{left:957px}
  .icon-bell{position:absolute;left:1084px;top:16px}
  .icon-share{position:absolute;left:1126px;top:18px}

  .mainnav{position:absolute;left:48px;top:90px;display:flex;align-items:center;font-size:13px;font-weight:500;white-space:nowrap}
  .mainnav .item{color:var(--ink)}
  .mainnav .item.active{color:var(--sky)}
  .mainnav .sep{width:3px;height:3px;border-radius:50%;background:var(--sky);margin:0 9px}

  .search{position:absolute;left:775px;top:81px;width:374px;height:37px;border:1px solid var(--line);display:flex;align-items:center;justify-content:space-between;padding:0 12px 0 17px;font-size:11.5px;letter-spacing:.2px}

  .subnav{position:absolute;left:333px;top:123px;width:430px;height:36px;background:var(--sky);color:var(--white);display:flex;align-items:center;padding-left:15px;font-size:12.5px;font-weight:600;white-space:nowrap}
  .subnav::before{content:"";position:absolute;left:15px;top:-10px;border:10px solid transparent;border-top:0;border-bottom-color:var(--sky)}
  .subnav .sep{width:3px;height:3px;border-radius:50%;background:var(--white);margin:0 8px}

  .criteria{position:absolute;left:331px;top:189px;width:583px;height:701px;background:var(--sky);padding:18px 26px 0 25px}
  .criteria::before{content:"";position:absolute;left:35px;top:-14px;border:15px solid transparent;border-top:0;border-bottom-color:var(--sky)}
  .section-title{color:var(--white);font-size:21px;font-weight:600;line-height:28px;margin-bottom:16px}
  .section-title.next{margin-top:21px;margin-bottom:14px}
  .section-title.currency{margin-top:22px;margin-bottom:16px;padding-left:3px}
  .field-grid{display:grid;grid-template-columns:259px 259px;column-gap:14px;row-gap:12px}
  .field{height:40px;background:var(--white);display:flex;align-items:center;justify-content:space-between;padding:0 14px 0 13px;font-size:11px;color:var(--ink)}
  .field .caret{width:0;height:0;border-top:4px solid transparent;border-bottom:4px solid transparent;border-left:5px solid var(--ink)}
  .field-split{display:grid;grid-template-columns:124px 126px;column-gap:9px}
  .field.date-field{padding-right:10px}
</style>
</head>
<body>
  <header class="topbar">
    <div class="brand"><span class="brand-dot"></span>Silver Harbor Hotels &amp; Suites</div>
    <span class="welcome">Welcome Admin</span>
    <span class="date">Tuesday October 04.2017</span>
    <span class="top-btn intel">INTEL</span>
    <span class="top-btn planning">PLANNING</span>
    <svg class="icon-bell" width="28" height="26" viewBox="0 0 28 26" fill="none" stroke="#fff" stroke-width="1.3" aria-label="Notifications">
      <path d="M8 18 V11 a6 6 0 0 1 12 0 V18 l2 2 H6 Z"/><path d="M12 21 a2 2 0 0 0 4 0"/>
      <path d="M4 8 q-2 4 0 8 M24 8 q2 4 0 8"/>
    </svg>
    <svg class="icon-share" width="28" height="22" viewBox="0 0 28 22" fill="none" stroke="#fff" stroke-width="1.4" aria-label="Share">
      <path d="M12 4 H3 V20 H21 V14"/><path d="M8 15 q3 -8 13 -8 V3 l6 6 -6 6 v-4 q-8 -1 -13 4 Z"/>
    </svg>
  </header>

  <nav class="mainnav">
    <span class="item">Admin</span><span class="sep"></span>
    <span class="item active">Management</span><span class="sep"></span>
    <span class="item active">Rooms Performance</span><span class="sep"></span>
    <span class="item active">Revenue Summary</span><span class="sep"></span>
    <span class="item">Demand &amp; Risk</span><span class="sep"></span>
    <span class="item">Inventory Analysis</span><span class="sep"></span>
    <span class="item">Placeholder</span>
  </nav>

  <div class="search">
    <span>PROPERTY SEARCH</span>
    <svg width="14" height="14" viewBox="0 0 14 14" fill="none" stroke="#111a26" stroke-width="1.2"><circle cx="6" cy="6" r="4.8"/><path d="M9.5 9.5 L13 13"/></svg>
  </div>

  <nav class="subnav">
    <span>Rollup Criteria</span><span class="sep"></span>
    <span>Report Criteria</span><span class="sep"></span>
    <span>Edit View</span><span class="sep"></span>
    <span>Saved View</span><span class="sep"></span>
    <span>Export</span>
  </nav>

  <main class="criteria">
    <h2 class="section-title">Geographic / Management Regions</h2>
    <div class="field-grid">
      <div class="field">Select Division<span class="caret"></span></div>
      <div class="field">Select Group<span class="caret"></span></div>
      <div class="field">Select Region<span class="caret"></span></div>
      <div class="field">Select Property<span class="caret"></span></div>
      <div class="field">Select Area<span class="caret"></span></div>
      <div class="field">Select Property ID<span class="caret"></span></div>
      <div class="field">Select City<span class="caret"></span></div>
      <div class="field">Select Country<span class="caret"></span></div>
    </div>

    <h2 class="section-title next">Operational / BI Filters</h2>
    <div class="field-grid">
      <div class="field">Brands<span class="caret"></span></div>
      <div class="field-split">
        <div class="field date-field">Opening Date
          <svg width="13" height="13" viewBox="0 0 13 13" fill="none" stroke="#111a26" stroke-width="1"><rect x="1" y="2" width="11" height="10"/><path d="M1 5 H12 M4 1 V3 M9 1 V3 M4 7 H5 M6 7 H7 M8 7 H9 M4 9.5 H5 M6 9.5 H7 M8 9.5 H9"/></svg>
        </div>
        <div class="field date-field" style="justify-content:flex-end">
          <svg width="13" height="13" viewBox="0 0 13 13" fill="none" stroke="#111a26" stroke-width="1"><rect x="1" y="2" width="11" height="10"/><path d="M1 5 H12 M4 1 V3 M9 1 V3 M4 7 H5 M6 7 H7 M8 7 H9 M4 9.5 H5 M6 9.5 H7 M8 9.5 H9"/></svg>
        </div>
      </div>
      <div class="field">Rating<span class="caret"></span></div>
      <div class="field-split">
        <div class="field">From</div>
        <div class="field">To<span class="caret"></span></div>
      </div>
      <div class="field">Hotel Type<span class="caret"></span></div>
      <div class="field">PMS System<span class="caret"></span></div>
      <div class="field">F&amp;B Service<span class="caret"></span></div>
      <div class="field">Finance System<span class="caret"></span></div>
    </div>

    <h2 class="section-title currency">Currency Conversion</h2>
    <div class="field-grid">
      <div class="field">Rollup Currency<span class="caret"></span></div>
      <div class="field">YOY Analysis<span class="caret"></span></div>
      <div class="field">Conversion Rate<span class="caret"></span></div>
      <div class="field">Same Store<span class="caret"></span></div>
    </div>
  </main>
</body>
</html>
```